Bright Arch Group business card

Bright Arch Group is the parent company of Bright Arch Building, Bright Arch Plumbing and Bright Arch Renovating. We require a sophisticated business card that covers all aspects of the building and plumbing space without using told or construction items.

Industry/Entity Type

Construction Company

Contact Information for Business Card

Gareth Pimley
Director
0472915083
gareth@brightarch.com.au
Www.brightarch.com.au

Font styles to use
Serif
Sans Serif

Colors
3176b5
ffce3e
0692cd
34a7d8
fbee3e
faa54b

Requirements
Must have
• Logo on front
• Logo and details on rear.
Nice to have
• Maybe water mark or shadow effect with logo
Should not have
• Tools or any construction associated items

```html
<!DOCTYPE html>
<html lang="en">
<head>
<meta charset="utf-8">
<title>Bright Arch Group – Business Card</title>
<link rel="stylesheet" href="https://fonts.googleapis.com/css2?family=Libre+Baskerville:wght@700&family=Raleway:wght@300;700&display=swap">
<style>
  :root {
    --backdrop: #e9e4dc;
    --orange-deep: #e5861c;
    --orange-mid: #f0a62f;
    --orange-light: #f5c24c;
    --card-black: #0b0b0b;
    --ink-white: #ffffff;
    --ink-soft: rgba(255, 255, 255, 0.88);
    --mark-faint: rgba(255, 255, 255, 0.28);
    --mark-silver: #d9d9d9;
  }
  * { margin: 0; padding: 0; box-sizing: border-box; }
  html, body {
    width: 1200px;
    height: 1023px;
    overflow: hidden;
    background: var(--backdrop);
  }
  .canvas {
    position: relative;
    width: 1200px;
    height: 1023px;
  }
  .card {
    position: absolute;
    width: 540px;
    height: 310px;
    border-radius: 4px;
    box-shadow: 0 14px 30px rgba(0, 0, 0, 0.22);
    overflow: hidden;
  }

  /* Front: orange details card */
  .card--details {
    left: 50px;
    top: 220px;
    background: linear-gradient(125deg, var(--orange-deep) 0%, var(--orange-mid) 40%, var(--orange-light) 70%, var(--orange-deep) 100%);
  }
  .watermark {
    position: absolute;
    left: 30px;
    bottom: 34px;
    font-family: "Raleway", sans-serif;
    font-weight: 300;
    font-size: 40px;
    letter-spacing: 3px;
    color: var(--mark-faint);
    white-space: nowrap;
  }
  .person {
    position: absolute;
    right: 40px;
    top: 38px;
    text-align: right;
  }
  .person__name {
    font-family: "Libre Baskerville", serif;
    font-weight: 700;
    font-size: 31px;
    color: var(--ink-white);
    line-height: 1.1;
  }
  .person__role {
    font-family: "Raleway", sans-serif;
    font-weight: 300;
    font-size: 22px;
    color: var(--ink-soft);
    margin-top: 4px;
  }
  .contact {
    position: absolute;
    right: 40px;
    top: 150px;
    text-align: right;
    font-family: "Raleway", sans-serif;
    font-weight: 700;
    color: var(--ink-white);
  }
  .contact__phone {
    display: flex;
    align-items: center;
    justify-content: flex-end;
    gap: 10px;
    font-size: 27px;
    letter-spacing: 0.5px;
  }
  .contact__phone svg { width: 18px; height: 24px; }
  .contact__line {
    font-size: 17px;
    margin-top: 8px;
  }

  /* Back: black logo card */
  .card--logo {
    left: 610px;
    top: 520px;
    background: var(--card-black);
    display: flex;
    align-items: center;
    justify-content: center;
  }
  .brand {
    display: flex;
    align-items: center;
    gap: 18px;
    font-family: "Raleway", sans-serif;
    font-weight: 300;
    font-size: 34px;
    letter-spacing: 6px;
    color: var(--mark-silver);
    text-transform: uppercase;
    white-space: nowrap;
  }
  .brand__dot {
    width: 26px;
    height: 26px;
    border-radius: 50%;
    background: var(--mark-silver);
  }
</style>
</head>
<body>
<main class="canvas">
  <section class="card card--details" aria-label="Business card front with contact details">
    <div class="watermark" aria-hidden="true">Bright Arch Group</div>
    <div class="person">
      <p class="person__name">Gareth Pimley</p>
      <p class="person__role">Director</p>
    </div>
    <div class="contact">
      <p class="contact__phone">
        <svg viewBox="0 0 18 24" aria-hidden="true">
          <path d="M6 2 C2 4 1 9 2 13 C3 18 7 22 11 22 L13 18 L10 16 L8 17 C6 15 5 11 6 8 L8 7 L8 3 Z" fill="#ffffff"/>
        </svg>
        0472915083
      </p>
      <p class="contact__line">gareth@brightarch.com.au</p>
      <p class="contact__line">www.brightarch.com.au</p>
    </div>
  </section>

  <section class="card card--logo" aria-label="Business card back with company name">
    <div class="brand">
      <span class="brand__dot" aria-hidden="true"></span>
      <span class="brand__name">Bright Arch Group</span>
    </div>
  </section>
</main>
</body>
</html>
```